Varnok Power Systems ( LED lIghting Service Company) flyer

A single sheet folded in half, like a book, highlighting LED lighting retrofits. Use stock pictures for different bulbs. We sell and install all fixtures. We install 48" tubes, corn bulbs, UFO lights, high bay lights, gas station canopy lights, parking lot lights,
Should include:
Reduce electric bill by as much as 70%
Improved quality of light
Zero maintenance cost
Eliminates eye strain and headache pain
Produces no heat
5 year warranty
Work with power companies to achieve greatest rebate.
Complete turnkey solution provider
Target Market(s)
Business owners, facility managers, VP of operations
Industry/Entity Type
It Company
Colors
Designer to choose colors to be used in the design.
Requirements
Must have
- High quality photos,
Nice to have
- Fonts, colors and designs are up to the designers

```html
<!DOCTYPE html>
<html lang="en">
<head>
<meta charset="utf-8">
<title>Varnok Power Systems – LED Lighting Brochure</title>
<link href="https://fonts.googleapis.com/css2?family=Exo+2:wght@500;700;800&family=Lato:ital,wght@0,400;0,700;1,400&display=swap" rel="stylesheet">
<style>
  :root{
    --bg:#ececec;
    --paper:#ffffff;
    --blue-top:#2f8fe0;
    --blue-bottom:#2a4aa8;
    --navy:#2b3593;
    --sky:#25a8e0;
    --teal-dark:#1f5f73;
    --warm:#6b4a2c;
    --ink:#2a2a2a;
    --brand:#1f5fc4;
    --white:#ffffff;
  }
  *{margin:0;padding:0;box-sizing:border-box}
  html,body{width:1200px;height:1200px;overflow:hidden;background:var(--bg)}
  .spread{position:absolute;left:40px;top:204px;width:1120px;height:792px;background:var(--paper);box-shadow:0 2px 10px rgba(0,0,0,.12);overflow:hidden}
  .spread-art{position:absolute;inset:0}
  .fold{position:absolute;left:560px;top:0;width:1px;height:100%;background:rgba(0,0,0,.06)}

  .about{position:absolute;left:100px;top:196px;width:430px;font-family:"Lato",sans-serif;color:var(--ink)}
  .about-title{font-family:"Exo 2",sans-serif;font-weight:700;font-style:italic;font-size:17px;color:var(--brand);margin-bottom:8px}
  .about-text{font-style:italic;font-size:12.5px;line-height:1.45;text-align:justify;margin-bottom:12px}
  .benefits{list-style:none;font-size:13px;line-height:1.3}
  .benefits li{display:flex;align-items:center;gap:8px;margin-bottom:6px}
  .benefits li strong{color:var(--brand)}
  .benefits svg{width:14px;height:14px;flex:none;fill:var(--brand)}

  .brand-name{position:absolute;font-family:"Exo 2",sans-serif;font-weight:800;color:var(--brand);line-height:1.05}
  .brand-name--cover{left:608px;top:60px;font-size:30px;width:230px}
  .brand-name--back{left:372px;top:562px;font-size:17px;color:var(--white);width:150px;text-align:right}

  .contacts{position:absolute;left:300px;top:622px;width:222px;list-style:none;font-family:"Lato",sans-serif;font-size:12.5px;color:var(--white)}
  .contacts li{display:flex;justify-content:flex-end;align-items:center;gap:10px;margin-bottom:7px}
  .contacts svg{width:13px;height:13px;fill:var(--white);flex:none}

  .cover-title{position:absolute;left:628px;top:392px;font-family:"Exo 2",sans-serif;color:var(--white);font-weight:500;font-size:34px;line-height:1.1}
  .cover-title .highlight{display:inline-block;margin-top:6px;margin-left:-8px;padding:0 12px;background:var(--white);color:var(--brand);font-weight:800;border-radius:8px}

  .services{position:absolute;left:612px;top:548px;display:flex;gap:20px;font-family:"Lato",sans-serif;font-size:13px;color:var(--white);line-height:1.2}
  .services ul{list-style:none}
  .services li::before{content:"•";margin-right:6px}
  .services li.lead::before{content:none}
  .services .lead{margin-bottom:2px}
  .services .col-2{padding-top:24px}

  .cover-web{position:absolute;left:640px;top:658px;font-family:"Exo 2",sans-serif;font-size:13px;letter-spacing:4px;color:var(--white);padding-bottom:6px;border-bottom:1px solid rgba(255,255,255,.7)}
</style>
</head>
<body>
<main class="spread">
  <svg class="spread-art" viewBox="0 0 1120 792" width="1120" height="792">
    <defs>
      <linearGradient id="blueFill" x1="0" y1="0" x2="0" y2="1">
        <stop offset="0" stop-color="var(--blue-top)"/>
        <stop offset="1" stop-color="var(--blue-bottom)"/>
      </linearGradient>
      <linearGradient id="headerFade" x1="0" y1="0" x2="0" y2="1">
        <stop offset="0" stop-color="#7fcfe0"/>
        <stop offset=".6" stop-color="#d4eef4"/>
        <stop offset="1" stop-color="#ffffff"/>
      </linearGradient>
      <radialGradient id="warmGlow" cx=".5" cy=".5" r=".6">
        <stop offset="0" stop-color="#e8c89a"/>
        <stop offset="1" stop-color="var(--warm)"/>
      </radialGradient>
      <radialGradient id="tealGlow" cx=".55" cy=".6" r=".6">
        <stop offset="0" stop-color="#5fb7cc"/>
        <stop offset="1" stop-color="var(--teal-dark)"/>
      </radialGradient>
    </defs>

    <rect class="header-photo" x="0" y="0" width="560" height="180" fill="url(#headerFade)" role="img" aria-label="Photo of hanging light bulbs with a glowing CFL bulb on a soft cyan background"/>

    <polygon class="blue-field" points="700,300 1080,792 150,792" fill="url(#blueFill)"/>
    <polygon class="navy-corner" points="120,560 272,762 0,792 0,700" fill="var(--navy)"/>
    <rect class="sky-diamond" x="163" y="573" width="134" height="134" transform="rotate(45 230 640)" fill="var(--sky)"/>

    <polygon class="photo-large" points="1060,-30 1260,170 1060,370 860,170" fill="url(#tealGlow)" stroke="var(--paper)" stroke-width="12" role="img" aria-label="Photo of LED bulbs hanging on cords against a dark teal background"/>
    <polygon class="photo-warm" points="850,150 950,250 850,350 750,250" fill="url(#warmGlow)" stroke="var(--paper)" stroke-width="12" role="img" aria-label="Photo of a glowing incandescent bulb on a warm brown background"/>
    <polygon class="photo-teal" points="960,350 1060,450 960,550 860,450" fill="url(#tealGlow)" stroke="var(--paper)" stroke-width="12" role="img" aria-label="Photo of several clear bulbs hanging in teal light"/>
    <polygon class="sky-diamond" points="1040,560 1125,645 1040,730 955,645" fill="var(--sky)"/>
    <rect x="1112" y="0" width="8" height="792" fill="var(--paper)"/>
  </svg>
  <div class="fold"></div>

  <section class="about">
    <h2 class="about-title">About Us</h2>
    <p class="about-text">Varnok Power Systems is a complete turnkey solution provider for LED lighting retrofits. We sell and install all fixtures, and we work with power companies to achieve the greatest rebate for your business.</p>
    <ul class="benefits">
      <li><svg viewBox="0 0 24 24"><path d="M9 16.2l-4.2-4.2-1.4 1.4L9 19 21 7l-1.4-1.4z"/></svg><span><strong>Reduce electric bill by as much as 70%</strong></span></li>
      <li><svg viewBox="0 0 24 24"><path d="M9 16.2l-4.2-4.2-1.4 1.4L9 19 21 7l-1.4-1.4z"/></svg><span>Improved quality of light</span></li>
      <li><svg viewBox="0 0 24 24"><path d="M9 16.2l-4.2-4.2-1.4 1.4L9 19 21 7l-1.4-1.4z"/></svg><span>Zero maintenance cost</span></li>
      <li><svg viewBox="0 0 24 24"><path d="M9 16.2l-4.2-4.2-1.4 1.4L9 19 21 7l-1.4-1.4z"/></svg><span>Eliminates eye strain and headache pain</span></li>
      <li><svg viewBox="0 0 24 24"><path d="M9 16.2l-4.2-4.2-1.4 1.4L9 19 21 7l-1.4-1.4z"/></svg><span>Produces no heat</span></li>
      <li><svg viewBox="0 0 24 24"><path d="M9 16.2l-4.2-4.2-1.4 1.4L9 19 21 7l-1.4-1.4z"/></svg><span><strong>5 year warranty</strong></span></li>
    </ul>
  </section>

  <div class="brand-name brand-name--back">Varnok Power Systems</div>
  <ul class="contacts">
    <li>your ph no. goes here <svg viewBox="0 0 24 24"><path d="M6.6 10.8a15 15 0 0 0 6.6 6.6l2.2-2.2c.3-.3.7-.4 1-.2 1.1.4 2.3.6 3.6.6.6 0 1 .4 1 1V20c0 .6-.4 1-1 1A17 17 0 0 1 3 4c0-.6.4-1 1-1h3.5c.6 0 1 .4 1 1 0 1.3.2 2.5.6 3.6.1.3 0 .7-.2 1z"/></svg></li>
    <li>your website goes here <svg viewBox="0 0 24 24"><path d="M12 2a10 10 0 1 0 0 20 10 10 0 0 0 0-20zm6.9 6h-3a15 15 0 0 0-1.3-3.9A8 8 0 0 1 18.9 8zM12 4c.8 1.2 1.5 2.5 1.9 4h-3.8c.4-1.5 1.1-2.8 1.9-4zM4.3 14a8 8 0 0 1 0-4h3.4a16 16 0 0 0 0 4zm.8 2h3a15 15 0 0 0 1.3 3.9A8 8 0 0 1 5.1 16zm3-8h-3a8 8 0 0 1 4.3-3.9A15 15 0 0 0 8.1 8zM12 20c-.8-1.2-1.5-2.5-1.9-4h3.8c-.4 1.5-1.1 2.8-1.9 4zm2.3-6H9.7a14 14 0 0 1 0-4h4.6a14 14 0 0 1 0 4zm.3 5.9a15 15 0 0 0 1.3-3.9h3a8 8 0 0 1-4.3 3.9zm1.7-5.9a16 16 0 0 0 0-4h3.4a8 8 0 0 1 0 4z"/></svg></li>
    <li>your mail goes here <svg viewBox="0 0 24 24"><path d="M3 5h18v14H3zm2 2v.5l7 4.5 7-4.5V7zm0 2.9V17h14V9.9l-7 4.5z"/></svg></li>
    <li>your address goes here <svg viewBox="0 0 24 24"><path d="M12 3l10 9h-3v8h-5v-6h-4v6H5v-8H2z"/></svg></li>
  </ul>

  <div class="brand-name brand-name--cover">Varnok Power Systems</div>

  <h1 class="cover-title">Varnok<br>Power<br><span class="highlight">Systems</span></h1>

  <div class="services">
    <ul class="col-1">
      <li class="lead">We install 48"</li>
      <li>Tubes</li>
      <li>Corn bulbs</li>
      <li>UFO lights</li>
    </ul>
    <ul class="col-2">
      <li>High bay lights</li>
      <li>Gas station canopy lights</li>
      <li>Parking lot lights</li>
    </ul>
  </div>

  <div class="cover-web">your website goes here</div>
</main>
</body>
</html>
```